Finance Product Agency Business Card Design

We're an agency that provides products (service contracts, gap insurance, tire and wheel, etc) and support to dealership finance departments. We specialize in training finance producers to maximize their potential and also keep them up to date on the ever changing compliance and legal landscape. I'll attach an image of our logo, excited to see what you all come up with. Would also be interested in discussing our new website design with the winner.

Target Market(s)

auto dealerships

Industry/Entity Type

Business

Contact Information for Business Card

Mark Dolvery
Phone 317.624.5583
Fax 855.472.3308
email Mark.Dolvery@brightlanecoverage.example

Requirements
Must have
• basic contact information
Nice to have
• looking for something professional but modern

```html
<!DOCTYPE html>
<html lang="en">
<head>
<meta charset="utf-8">
<title>Brightlane Coverage – Business Card</title>
<link href="https://fonts.googleapis.com/css2?family=Questrial&display=swap" rel="stylesheet">
<style>
  :root {
    --backdrop: #2a2a2c;
    --card: #141415;
    --card-edge: #1d1d1f;
    --accent: #3f7f95;
    --text-light: #d9d9d9;
    --silver: #9a9a9c;
    --brand-white: #e8e8e8;
  }
  * { margin: 0; padding: 0; box-sizing: border-box; }
  html, body {
    width: 1200px; height: 786px; overflow: hidden;
    background: var(--backdrop);
    font-family: "Questrial", "Century Gothic", sans-serif;
  }
  .sheet {
    width: 1200px; height: 786px;
    display: flex; flex-direction: column;
    align-items: center; justify-content: center; gap: 40px;
  }
  .card {
    position: relative;
    width: 620px; height: 354px;
    background: var(--card);
    border: 1px solid var(--card-edge);
    border-radius: 4px;
    box-shadow: 0 10px 30px rgba(0,0,0,.45);
  }
  /* Front */
  .card--front { display: flex; align-items: center; justify-content: center; }
  .brand { display: flex; align-items: center; gap: 14px; }
  .brand__mark {
    width: 34px; height: 34px; border-radius: 50%;
    background: var(--silver);
  }
  .brand__name {
    font-size: 34px; letter-spacing: 1px;
    color: var(--silver); text-transform: uppercase;
  }
  /* Back */
  .card--back .brand {
    position: absolute; right: 44px; top: 78px;
  }
  .card--back .brand__mark { background: var(--accent); width: 30px; height: 30px; }
  .card--back .brand__name { color: var(--brand-white); font-size: 28px; }
  .person { position: absolute; left: 44px; top: 150px; }
  .person__name {
    color: var(--accent); font-size: 15px;
    text-transform: uppercase; letter-spacing: 1px;
  }
  .person__title { color: var(--text-light); font-size: 14px; margin-top: 4px; }
  .contacts {
    position: absolute; left: 44px; right: 44px; bottom: 56px;
    display: flex; gap: 40px;
  }
  .contact-list { list-style: none; }
  .contact-list li {
    display: flex; align-items: center; gap: 9px;
    color: var(--text-light); font-size: 14px; line-height: 24px;
  }
  .icon { width: 15px; height: 15px; flex: none; }
</style>
</head>
<body>
<main class="sheet">
  <section class="card card--front" aria-label="Card front">
    <div class="brand">
      <span class="brand__mark"></span>
      <span class="brand__name">Brightlane Coverage</span>
    </div>
  </section>

  <section class="card card--back" aria-label="Card back">
    <div class="brand">
      <span class="brand__mark"></span>
      <span class="brand__name">Brightlane Coverage</span>
    </div>

    <div class="person">
      <p class="person__name">Mark Dolvery</p>
      <p class="person__title">General Manager</p>
    </div>

    <div class="contacts">
      <ul class="contact-list">
        <li>
          <svg class="icon" viewBox="0 0 16 16"><rect width="16" height="16" rx="2" fill="#3f7f95"/><path d="M5 3.5l2 2-1.2 1.2c.6 1.3 1.5 2.2 2.8 2.8L9.8 8.3l2 2-1.3 1.7C7.2 11.6 4.4 8.8 4 5.5z" fill="#141415"/></svg>
          317.624.5583
        </li>
        <li>
          <svg class="icon" viewBox="0 0 16 16"><rect width="16" height="16" rx="2" fill="#3f7f95"/><rect x="4" y="3" width="8" height="4" fill="#141415"/><rect x="3" y="7" width="10" height="6" rx="1" fill="#141415"/></svg>
          855.472.3308
        </li>
      </ul>
      <ul class="contact-list">
        <li>
          <svg class="icon" viewBox="0 0 16 16"><rect width="16" height="16" rx="2" fill="#3f7f95"/><rect x="3" y="4.5" width="10" height="7" fill="#141415"/><path d="M3 4.5l5 4 5-4" stroke="#3f7f95" fill="none"/></svg>
          Mark.Dolvery@brightlanecoverage.example
        </li>
        <li>
          <svg class="icon" viewBox="0 0 16 16"><rect width="16" height="16" rx="2" fill="#3f7f95"/><circle cx="8" cy="8" r="4.5" fill="none" stroke="#141415" stroke-width="1.3"/><path d="M3.5 8h9M8 3.5c-2 2.5-2 6.5 0 9M8 3.5c2 2.5 2 6.5 0 9" stroke="#141415" fill="none"/></svg>
          www.brightlanecoverage.example
        </li>
      </ul>
    </div>
  </section>
</main>
</body>
</html>
```